Label

I need a label designed for a bottle of water. I like the lightning bolt and the blue. But I do not want it exactly like the Zimm-ooh.

The label needs to be 9 inches by 2.5 inches.

Logo Text

Mesa Spring: Sip the Mesa

```html
<!DOCTYPE html>
<html lang="en">
<head>
<meta charset="utf-8">
<title>Mesa Spring – Bottle Label</title>
<link rel="stylesheet" href="https://fonts.googleapis.com/css2?family=Bebas+Neue&display=swap">
<style>
  :root {
    --label-blue: #0096c9;
    --band-light: #3aaad7;
    --band-dark: #0a78a4;
    --name-white: #f5f5f5;
    --tagline-grey: #d9d9d9;
    --mark-white: #f0f0f0;
    --volume-white: #ffffff;
  }
  html, body {
    margin: 0;
    padding: 0;
    overflow: hidden;
    background: #ffffff;
  }
  .label {
    position: relative;
    width: 1200px;
    height: 333px;
    background: var(--label-blue);
    overflow: hidden;
    font-family: "Bebas Neue", "Oswald", sans-serif;
  }
  .brand-mark {
    position: absolute;
    left: 800px;
    top: 22px;
    width: 108px;
    height: 108px;
    border-radius: 50%;
    background: var(--mark-white);
  }
  .brand-name {
    position: absolute;
    left: 396px;
    top: 108px;
    margin: 0;
    font-size: 95px;
    font-weight: 400;
    line-height: 1;
    letter-spacing: 0.5px;
    color: var(--name-white);
    white-space: nowrap;
  }
  .tagline {
    position: absolute;
    left: 398px;
    top: 199px;
    margin: 0;
    font-size: 31px;
    font-weight: 400;
    line-height: 1;
    letter-spacing: 0.5px;
    color: var(--tagline-grey);
    white-space: nowrap;
  }
  .volume-band {
    position: absolute;
    left: 0;
    top: 284px;
    width: 1200px;
    height: 49px;
    background: linear-gradient(90deg, var(--band-light), var(--band-dark));
  }
  .volume {
    position: absolute;
    left: 758px;
    top: 15px;
    margin: 0;
    display: flex;
    align-items: center;
    gap: 4px;
    font-size: 19px;
    line-height: 1;
    color: var(--volume-white);
    white-space: nowrap;
  }
  .volume-icon {
    width: 11px;
    height: 15px;
  }
</style>
</head>
<body>
  <main class="label">
    <div class="brand-mark" aria-hidden="true"></div>
    <h1 class="brand-name">Mesa Spring</h1>
    <p class="tagline">Sip the Mesa</p>
    <div class="volume-band">
      <p class="volume">
        <svg class="volume-icon" viewBox="0 0 11 15" aria-hidden="true">
          <path d="M5.5 0 C5.5 0 0 7 0 9.5 A5.5 5.5 0 0 0 11 9.5 C11 7 5.5 0 5.5 0 Z" fill="#ffffff"/>
        </svg>
        1 Liter (33.8 fl. oz)
      </p>
    </div>
  </main>
</body>
</html>
```